Web Design for historic veg friendly, organic restaurant

We need a new web site. The Millbrook Cafe is a 40 year old restaurant in Chicago. We've been one of the premier, casual vegetarian restaurants since we opened. 5 years ago, Millbrook Cafe was purchased from the original owners by a local, certified organic farmer. We are nearly 100% from scratch kitchen, 100% certified organic produce, we are governed by a strict sustainable plan and we are very active politically. But you wouldn't know it form our website! We have a desire to build a simple website around some basic principles:
1. We need our current logo prominently displayed (logo attached)
2. We need a "click to call" easily accessible
3. We have an online order link that needs to be easily accessible
4. We need our hours, location, and directions easy to see
4. We need a separate events page (we have a live music and events venue that runs shows 5-7 nights per week.)
5. We would like to have a separate page for pictures, particularly old pictures. It would be fun to have a function for people to post their own shots, but that might make this too complicated. If it were possible, we would of course need to retain the ability to curate posted pictures.
6. This needs to be easily edited by us, so in a platform such as word press or similar
7. We will need this mobile enhanced

Target Market(s)

Neighborhood residents - zip code is 48213

Industry/Entity Type

Restaurant

Coding

Coded - Design and coding required

Number of Pages Required

4 page

Font styles to use
Sans Serif

Requirements
Must have
• Logo, click to call, events page that we can manage, contact us, about us page, menu (we have the online menu through a third party plugin), a page for our market and some nice pictures on our splash page,
• Must be mobile ready and on a platform such as Word Press or some other platform where we can edit on our own
Nice to have
• Page for past employees and historical pictures, be nice to have food pictures or something similar on a scroll, would love to have an ability for others to post pictures that we would "approve"
Should not have
• We don't need anything that spins, moves, flames or other features that detract from gathering information

```html
<!DOCTYPE html>
<html lang="en">
<head>
<meta charset="utf-8">
<title>Millbrook Cafe</title>
<link href="https://fonts.googleapis.com/css2?family=Nunito:wght@400;600;700&family=Open+Sans:wght@400;600&display=swap" rel="stylesheet">
<style>
:root{
  --red:#d23f3a;
  --red-dark:#b8322e;
  --ink:#222;
  --text:#555;
  --muted:#8a8a8a;
  --white:#fff;
  --light:#f4f4f4;
  --footer:#161616;
  --bottom:#050505;
  --rose:#c46a6e;
}
*{margin:0;padding:0;box-sizing:border-box}
html,body{width:1200px;height:2752px;overflow:hidden}
body{font-family:"Open Sans",Arial,sans-serif;color:var(--text);background:var(--white);position:relative}
.abs{position:absolute}
.heading{font-family:"Nunito",Arial,sans-serif;color:var(--ink);font-weight:400;text-transform:uppercase;letter-spacing:.5px}

/* header */
.site-header{position:absolute;left:0;top:0;width:1200px;height:156px;background:var(--white)}
.brand{left:86px;top:58px;display:flex;align-items:center;gap:12px}
.brand-dot{width:26px;height:26px;border-radius:50%;background:var(--red)}
.brand-name{font-family:"Nunito",Arial,sans-serif;font-weight:700;font-size:34px;color:var(--red)}
.topbar{right:78px;top:36px;display:flex;align-items:center;gap:14px}
.topbar .phone{font-family:"Nunito",sans-serif;font-size:21px;color:#333;display:flex;align-items:center;gap:8px;margin-left:16px;margin-right:10px}
.social{display:flex;gap:8px}
.social span{width:22px;height:22px;border-radius:3px;background:#9aa3ad;display:block}
.main-nav{top:89px;left:393px;display:flex;font-family:"Nunito",sans-serif;font-size:17px;color:#333}
.main-nav a{color:#333;text-decoration:none;position:absolute;white-space:nowrap}

/* hero */
.hero{position:absolute;left:0;top:156px;width:1200px;height:556px;
  background:radial-gradient(ellipse at 60% 40%,#5a3a2a 0%,#2c1c16 45%,#120c0a 100%)}
.hero-title{position:absolute;top:250px;width:100%;text-align:center;font-family:"Nunito",sans-serif;font-size:52px;color:var(--white);letter-spacing:1px}
.hero-sub{position:absolute;top:322px;width:100%;text-align:center;font-size:21px;color:var(--white)}
.btn{display:inline-block;background:var(--red);color:var(--white);font-family:"Nunito",sans-serif;text-transform:uppercase;border-radius:22px;text-align:center}
.hero .btn{position:absolute;left:523px;top:363px;width:154px;height:41px;line-height:41px;font-size:16px}
.hero-dots{position:absolute;left:1143px;top:264px;display:flex;flex-direction:column;gap:11px}
.hero-dots span{width:8px;height:8px;border-radius:50%;background:var(--white)}
.hero-dots span:first-child{background:var(--red)}

/* welcome */
.welcome-title{top:766px;width:100%;text-align:center;font-size:28px}
.welcome-text{left:187px;top:818px;width:826px;text-align:center;font-size:14px;line-height:24px;color:var(--muted)}
.feature{top:939px;width:300px;text-align:center}
.feature .icon{width:104px;height:104px;border-radius:50%;background:var(--red);margin:0 auto;display:flex;align-items:center;justify-content:center}
.feature h3{margin-top:28px;font-size:18px}
.feature p{margin-top:12px;font-size:13px;line-height:20px;color:var(--muted)}
.feature .more{display:block;margin-top:14px;font-size:14px;color:#333}

/* order band */
.order-band{position:absolute;left:0;top:1248px;width:1200px;height:449px;
  background:linear-gradient(90deg,#c77377,#c46a6e 50%,#bf6468)}
.order-card{position:absolute;left:150px;top:64px;width:507px;height:325px;background:var(--white);padding:50px 36px 0 36px}
.order-card h2{font-size:31px;color:var(--ink)}
.order-card .sub{font-size:16px;color:#333;margin-top:4px}
.order-card p{font-size:13.5px;line-height:22px;color:var(--text);margin-top:12px}
.order-actions{display:flex;align-items:center;gap:22px;margin-top:20px}
.order-actions .btn{width:108px;height:31px;line-height:31px;font-size:13px}
.order-actions .phone{font-family:"Nunito",sans-serif;font-size:21px;color:#333;display:flex;align-items:center;gap:8px}
.order-photo{position:absolute;left:657px;top:64px;width:393px;height:325px;
  background:linear-gradient(160deg,#6b4a2a 0%,#8a5a30 35%,#a85a3a 60%,#4e3520 100%)}

/* menu */
.menu-title{top:1766px;width:100%;text-align:center;font-size:28px}
.menu-card{top:1850px;width:243px;height:209px;background:var(--white);box-shadow:0 2px 5px rgba(0,0,0,.18)}
.menu-card .photo{height:164px}
.menu-card .label{height:45px;line-height:45px;text-align:center;font-family:"Nunito",sans-serif;font-size:15px;color:#333;text-transform:uppercase}

/* testimonials */
.testimonials{position:absolute;left:0;top:2129px;width:1200px;height:339px;background:var(--light)}
.testimonials .heading{position:absolute;top:50px;width:100%;text-align:center;font-size:28px}
.quote{position:absolute;top:132px;display:flex;gap:28px}
.avatar{width:94px;height:94px;border-radius:50%;background:linear-gradient(135deg,#b98a6e,#6a4634)}
.quote .body{width:312px;padding-top:20px}
.quote blockquote{font-size:13.5px;line-height:22px;color:#666;text-indent:4px}
.quote .mark{color:var(--red);font-family:"Nunito",sans-serif;font-size:22px;line-height:0}
.quote .name{margin-top:12px;font-size:12.5px;color:var(--red);text-transform:uppercase;font-weight:600}
.quote .role{font-size:12.5px;color:#555;margin-top:4px}

/* footer */
.site-footer{position:absolute;left:0;top:2468px;width:1200px;height:229px;background:var(--footer);color:var(--white)}
.foot-col{position:absolute;top:52px}
.foot-col h4{font-family:"Nunito",sans-serif;font-weight:400;font-size:16px;text-transform:uppercase;margin-bottom:14px}
.foot-col p{font-size:12px;line-height:22px}
.foot-map{position:absolute;left:881px;top:40px;width:238px;height:144px;background:linear-gradient(135deg,#e8e6e0,#d6d8d2)}
.bottom-bar{position:absolute;left:0;top:2697px;width:1200px;height:55px;background:var(--bottom);color:var(--white)}
.bottom-bar .copy{position:absolute;left:88px;top:18px;font-size:13px}
.bottom-bar .social{position:absolute;right:94px;top:17px}
.bottom-bar .social span{width:17px;height:17px;background:#cfcfcf}
</style>
</head>
<body>

<header class="site-header">
  <div class="brand abs"><span class="brand-dot"></span><span class="brand-name">Millbrook Cafe</span></div>
  <div class="topbar abs">
    <svg width="16" height="16" viewBox="0 0 16 16"><circle cx="6.5" cy="6.5" r="5" fill="none" stroke="#222" stroke-width="2"/><line x1="10" y1="10" x2="15" y2="15" stroke="#222" stroke-width="2.4"/></svg>
    <span class="phone"><svg width="18" height="18" viewBox="0 0 18 18"><rect width="18" height="18" rx="3" fill="#e0542a"/><path d="M5 4l2 0 1 3-1.3 1a7 7 0 0 0 3.3 3.3l1-1.3 3 1v2a1 1 0 0 1-1 1A9 9 0 0 1 4 5a1 1 0 0 1 1-1z" fill="#fff"/></svg>312-555-0147</span>
    <div class="social"><span></span><span></span><span></span><span></span></div>
  </div>
  <nav class="main-nav abs">
    <a style="left:0">HOME</a>
    <a style="left:82px">MENU</a>
    <a style="left:165px">LOCATION &amp; HOURS</a>
    <a style="left:354px">EVENTS</a>
    <a style="left:449px">ABOUT</a>
    <a style="left:541px">BOOKING</a>
    <a style="left:649px">CONTACT</a>
  </nav>
</header>

<section class="hero" role="img" aria-label="Photo of guests listening to live music in the dimly lit cafe">
  <h1 class="hero-title">MILLBROOK CAFE</h1>
  <p class="hero-sub">100% from scratch kitchen, 100% certified organic restaurant</p>
  <a class="btn">Click to call</a>
  <div class="hero-dots"><span></span><span></span><span></span><span></span><span></span></div>
</section>

<h2 class="heading welcome-title abs">Welcome to Millbrook Cafe</h2>
<p class="welcome-text abs">It is a long established fact that a reader will be distracted by the readable content of a page when looking at its layout. The point of using Lorem Ipsum is that it has a more-or-less normal distribution of letters, as opposed to using 'Content here, content here', making it look like readable English. Many desktop publishing packages and web page editors</p>

<div class="feature abs" style="left:125px">
  <div class="icon"><svg width="48" height="48" viewBox="0 0 48 48"><path d="M8 8h32L26 24v14h8v3H14v-3h8V24z" fill="#fff"/></svg></div>
  <h3 class="heading">Organic Restaurant</h3>
  <p>It has survived not only five centuries, but also the leap into electronic typesetting.</p>
  <span class="more">Learn More -&gt;</span>
</div>
<div class="feature abs" style="left:456px">
  <div class="icon"><svg width="44" height="44" viewBox="0 0 44 44"><g fill="#fff"><circle cx="22" cy="22" r="13"/><rect x="18" y="3" width="8" height="38" rx="2"/><rect x="18" y="3" width="8" height="38" rx="2" transform="rotate(45 22 22)"/><rect x="18" y="3" width="8" height="38" rx="2" transform="rotate(90 22 22)"/><rect x="18" y="3" width="8" height="38" rx="2" transform="rotate(135 22 22)"/></g><circle cx="22" cy="22" r="5.5" fill="#d23f3a"/></svg></div>
  <h3 class="heading">Services</h3>
  <p>It has survived not only five centuries, but also the leap into electronic typesetting.</p>
  <span class="more">Learn More -&gt;</span>
</div>
<div class="feature abs" style="left:786px">
  <div class="icon"><svg width="48" height="48" viewBox="0 0 48 48"><path d="M30 10H12a3 3 0 0 0-3 3v23a3 3 0 0 0 3 3h23a3 3 0 0 0 3-3V22" fill="none" stroke="#fff" stroke-width="3.5"/><path d="M36 6l6 6-17 17-8 2 2-8z" fill="#fff"/></svg></div>
  <h3 class="heading">Booking</h3>
  <p>It has survived not only five centuries, but also the leap into electronic typesetting.</p>
  <span class="more">Learn More -&gt;</span>
</div>

<section class="order-band" role="img" aria-label="Rose-tinted photo of the busy dining room">
  <div class="order-card">
    <h2 class="heading">Order Online Now!</h2>
    <div class="sub">Online ordering for pickup only</div>
    <p>It is a long established fact that a reader will be distracted by the readable content of a page when looking at its layout. The point of using Lorem Ipsum is that it has a more-or-less normal distribution of letters, as opposed to using 'Content here, content here', making it look like readable English. Many desktop publishing packages</p>
    <div class="order-actions">
      <a class="btn">Order Now</a>
      <span class="phone"><svg width="16" height="16" viewBox="0 0 18 18"><path d="M3 1l4 0 1.5 4.5-2 1.5a10 10 0 0 0 4.5 4.5l1.5-2 4.5 1.5v4a1 1 0 0 1-1 1A15 15 0 0 1 2 2a1 1 0 0 1 1-1z" fill="#e07a6a"/></svg>312-555-0182</span>
    </div>
  </div>
  <div class="order-photo" role="img" aria-label="Photo of market shelves stocked with fresh vegetables and fruit"></div>
</section>

<h2 class="heading menu-title abs">Our Menu</h2>
<div class="menu-card abs" style="left:94px"><div class="photo" role="img" aria-label="Photo of a breakfast plate" style="background:linear-gradient(135deg,#c98a4a,#8a5a2e)"></div><div class="label">Breakfast</div></div>
<div class="menu-card abs" style="left:352px"><div class="photo" role="img" aria-label="Photo of a lunch dish with greens" style="background:linear-gradient(135deg,#4a5a2a,#2a2a1a)"></div><div class="label">Lunch</div></div>
<div class="menu-card abs" style="left:611px"><div class="photo" role="img" aria-label="Photo of a dinner salad with tomatoes" style="background:linear-gradient(135deg,#d89a5a,#b04030)"></div><div class="label">Dinner</div></div>
<div class="menu-card abs" style="left:870px"><div class="photo" role="img" aria-label="Photo of a baked side dish with chips" style="background:linear-gradient(135deg,#e0b060,#8a4a1e)"></div><div class="label">Others</div></div>

<section class="testimonials">
  <h2 class="heading">Testimonials</h2>
  <div class="quote" style="left:104px">
    <div class="avatar" role="img" aria-label="Portrait of a guest"></div>
    <div class="body">
      <blockquote><span class="mark">&ldquo;</span> Ipsum has been the industry's standard dummy text ever since the 1500s, when an unknown printer took a galley of type and scrambled <span class="mark">&rdquo;</span></blockquote>
      <div class="name">Lena Marsh</div>
      <div class="role">Marketing Executive</div>
    </div>
  </div>
  <div class="quote" style="left:659px">
    <div class="avatar" role="img" aria-label="Portrait of a guest"></div>
    <div class="body">
      <blockquote><span class="mark">&ldquo;</span> Ipsum has been the industry's standard dummy text ever since the 1500s, when an unknown printer took a galley of type and scrambled it to make <span class="mark">&rdquo;</span></blockquote>
      <div class="name">Lena Marsh</div>
      <div class="role">Marketing Executive</div>
    </div>
  </div>
</section>

<footer class="site-footer">
  <div class="foot-col" style="left:92px">
    <h4>Seasonal Dining Hours</h4>
    <p>MONDAY – FRIDAY &nbsp; 9 am – 10 pm<br>SATURDAY and SUNDAY &nbsp; 8 am – 10 pm</p>
  </div>
  <div class="foot-col" style="left:367px">
    <h4>The Cedar Bar</h4>
    <p>MONDAY – TUESDAY &nbsp; 11 am – 10 pm<br>WEDNESDAY &nbsp; 11 am – 12 AM<br>FRIDAY/SATURDAY &nbsp; 10 am – 12 am<br>SUNDAY &nbsp; 10 am – 10 pm</p>
  </div>
  <div class="foot-col" style="left:629px">
    <h4>Contact Us</h4>
    <p>Address : 2150 W. Alder Ave &nbsp;|<br>Chicago, IL | 48213<br>Phone : &nbsp;312-555-0182<br>Email : hello@millbrookcafe.com</p>
  </div>
  <div class="foot-map" role="img" aria-label="Street map showing the cafe location"></div>
</footer>

<div class="bottom-bar">
  <span class="copy">Copyright © 2017. All Rights Reserved</span>
  <div class="social"><span></span><span></span><span></span><span></span></div>
</div>

</body>
</html>
```